WebSite

Hi,

I need a (responsive?) website for a company that has 3 core businesses:

Hosting
Web design (also logo design)
and ICT systems management

The hosting part has a whois that can be searched, and from there a domain can be registered or moved if it is taken and the move code is known.
Also a pricelist for the 4 different types of packages + add-ons.

The web design part has got to have a small portfolio section.

The ICT management section is just an ordinary page with some info on the work the company does.

And off course a contact page...

http://sh1.vq-serverhuis.nl/cgi-sys/defaultwebpage.cgi

It is a Dutch company, the logo is provided.

I like clean designs, not to busy or to dark, just good look and feel and modern!

I like those single page (with pages that flout into each other etc.) designs (like: http://www.gullweave.com/tovu) but that kind of sites needs to be coded also, that would be part of the job than!

This is my first time here so I do not know if more information is needed or what happens next :)
Updates

http://lomberquay.com/#!portfolio-dmesk to give another example of what I like, a site like that is great! 

Hello,

I recieved some designs already but I was hoping for some more creativity, I do not want a design I can buy at Layoutgrotto, I really am in need for something that goes with my logo and looks unique (see last link from brief).

Industry/Entity Type

It Company

Logo Text

VQ Services

```html
<!DOCTYPE html>
<html lang="en">
<head>
<meta charset="utf-8">
<title>VQ Services</title>
<link href="https://fonts.googleapis.com/css2?family=Open+Sans:wght@400;600;700&display=swap" rel="stylesheet">
<style>
:root{
  --blue:#1a5b99;
  --blue-dark:#134a80;
  --navy:#132c4b;
  --navy-deep:#0c1c33;
  --ink:#222;
  --muted:#444;
  --line:#e4e4e4;
  --card:#fbfbfb;
  --footer:#3b3b3b;
}
*{box-sizing:border-box;margin:0;padding:0}
html,body{width:829px;height:1200px;overflow:hidden;background:#fff;font-family:'Open Sans',sans-serif;color:var(--ink)}
.page{position:relative;width:829px;height:1200px}
.abs{position:absolute}
.site-header{left:0;top:0;width:829px;height:84px;background:#fff}
.brand{left:120px;top:20px;display:flex;align-items:center;gap:8px;font-weight:700;font-size:17px;color:var(--blue)}
.brand-dot{width:26px;height:26px;border-radius:50%;background:var(--blue)}
.contact-line{top:39px;font-size:8.5px;color:var(--ink);display:flex;align-items:center;gap:6px}
.main-nav{left:0;top:84px;width:829px;height:37px;background:var(--blue);border-top:3px solid #4a4a4a}
.nav-home{left:120px;top:0;width:56px;height:34px;background:#f2f2f2;display:flex;align-items:center;justify-content:center}
.nav-item{top:0;height:34px;line-height:34px;color:#fff;font-size:8.5px;font-weight:600;border-right:1px solid rgba(255,255,255,.12);text-align:center}
.hero{left:0;top:121px;width:829px;height:333px;background:radial-gradient(ellipse at 50% 70%,#24466e 0%,var(--navy) 55%,var(--navy-deep) 100%)}
.hero-title{left:0;top:36px;width:829px;text-align:center;color:#fff;font-weight:600;font-size:33px;letter-spacing:.3px}
.hero-title small{font-size:20px;font-weight:700}
.hero-text{left:120px;top:86px;width:589px;text-align:center;color:#e8eef6;font-size:8.2px;line-height:13px}
.btn-hero{left:352px;top:126px;width:125px;height:32px;background:var(--blue);border-radius:4px;color:#fff;font-size:10.5px;line-height:32px;text-align:center}
.hero-arrow{top:151px;width:30px;height:30px;border-radius:50%;background:#0b1524;display:flex;align-items:center;justify-content:center}
.hero-arrow span{width:20px;height:20px;border-radius:50%;background:#eee;display:flex;align-items:center;justify-content:center}
.hero-media{left:235px;top:189px;width:358px;height:144px;background:linear-gradient(90deg,#9ea4ab,#2b2f35 30%,#1b1d21 50%,#2b2f35 70%,#c7ccd1)}
.service-card{top:478px;width:184px;height:208px;background:var(--card);border:1px solid #e6e6e6;box-shadow:0 4px 4px -3px rgba(0,0,0,.2);text-align:center}
.service-icon{position:absolute;left:52px;top:14px;width:80px;height:80px;border-radius:50%;background:#f1f1f1;box-shadow:inset 0 0 0 3px #e9e9e9;display:flex;align-items:center;justify-content:center}
.service-title{position:absolute;left:0;top:100px;width:100%;font-size:11.2px;font-weight:600}
.service-text{position:absolute;left:14px;top:124px;width:156px;font-size:7px;line-height:13px;color:var(--muted)}
.btn-small{position:absolute;left:66px;top:173px;width:50px;height:22px;background:var(--blue);border-radius:4px;color:#fff;font-size:7px;font-weight:600;line-height:22px}
.section-title{top:712px;font-size:14px;font-weight:400}
.section-title b{color:var(--blue);font-weight:600}
.rule{top:742px;height:1px;background:var(--line)}
.welcome-media{left:118px;top:760px;width:270px;height:136px;border:3px solid #fff;outline:1px solid #ddd;background:linear-gradient(180deg,#8fb6de 0%,#cfe0ef 45%,#2f3a48 75%,#5a6b7d 100%)}
.welcome-text{left:119px;top:906px;width:268px;font-size:7px;line-height:13px;color:var(--muted);text-align:justify}
.btn-dark{left:119px;top:1009px;width:68px;height:24px;background:#444;border-radius:3px;color:#fff;font-size:8.5px;line-height:24px;text-align:center}
.news-item{left:426px;width:284px;height:128px;border:1px solid #e6e6e6;background:var(--card)}
.news-photo{position:absolute;left:12px;top:12px;width:94px;height:88px;border:3px solid #fff;outline:1px solid #ddd}
.news-title{position:absolute;left:120px;top:11px;font-size:10.5px}
.news-date{position:absolute;left:120px;top:36px;font-size:6.5px}
.news-text{position:absolute;left:120px;top:54px;width:152px;font-size:7px;line-height:13px;color:var(--muted);text-align:justify}
.news-more{position:absolute;right:14px;top:108px;font-size:7px;font-weight:600;color:var(--blue)}
.partners{left:118px;top:1056px;width:593px;height:59px;border:1px solid #e6e6e6;display:flex;align-items:center;justify-content:space-around}
.partner{display:flex;align-items:center;gap:6px;font-size:13px;font-weight:600;color:#bdbdbd}
.partner i{width:18px;height:18px;border-radius:50%;background:#d6d6d6;display:block}
.site-footer{left:0;top:1136px;width:829px;height:64px;background:var(--footer);border-bottom:2px solid var(--blue)}
.footer-brand{left:120px;top:20px;font-size:10px;font-weight:700;color:#ccc}
.footer-nav{left:201px;top:17px;font-size:7.2px;color:#eee;word-spacing:2px}
.footer-copy{left:201px;top:39px;font-size:6.8px;color:#ddd}
.social{top:21px;width:22px;height:22px;border-radius:50%;border:2px solid #2a2a2a}
</style>
</head>
<body>
<div class="page">

  <header class="abs site-header">
    <div class="abs brand"><span class="brand-dot"></span>VQ Services</div>
    <div class="abs contact-line" style="left:488px">
      <svg width="9" height="10" viewBox="0 0 10 10"><path d="M2 0l2 2.5-1.2 1.2a6 6 0 003.5 3.5L7.5 6 10 8l-1.2 2C4.5 10 0 5.5 0 1.2z" fill="#222"/></svg>
      Call Us : 078-5512093
    </div>
    <div class="abs contact-line" style="left:613px">
      <svg width="10" height="8" viewBox="0 0 10 8"><rect width="10" height="8" fill="#222"/><path d="M0 0l5 4 5-4" stroke="#fff" fill="none"/></svg>
      Sales@VQ-Services.nl
    </div>
  </header>

  <nav class="abs main-nav">
    <div class="abs nav-home">
      <svg width="18" height="15" viewBox="0 0 18 15"><path d="M9 0L0 8h2.5v7h4.5v-5h4v5h4.5V8H18z" fill="#111"/></svg>
    </div>
    <div class="abs nav-item" style="left:176px;width:79px">ABOUT</div>
    <div class="abs nav-item" style="left:255px;width:75px">SERVICES</div>
    <div class="abs nav-item" style="left:330px;width:102px">WEBHOSTING</div>
    <div class="abs nav-item" style="left:432px;width:113px">AUTOMATISERING</div>
    <div class="abs nav-item" style="left:545px;width:92px;border-right:0">CONTACT US</div>
  </nav>

  <section class="abs hero">
    <h1 class="abs hero-title">VQ SERVICES <small>TO DELIVER BUSINESS VALUE!</small></h1>
    <p class="abs hero-text">Management, Leadership and Team Building for Business Analysts and Program Managers. Management, Leadership and Team Building for Business Analysts and Program Managers. Management, Leadership and Team Building for Business Analysts and Program Managers.</p>
    <div class="abs btn-hero">GET STARTED NOW</div>
    <div class="abs hero-arrow" style="left:54px"><span><svg width="6" height="8" viewBox="0 0 6 8"><path d="M5 0L1 4l4 4" stroke="#666" fill="none" stroke-width="1.5"/></svg></span></div>
    <div class="abs hero-arrow" style="left:741px"><span><svg width="6" height="8" viewBox="0 0 6 8"><path d="M1 0l4 4-4 4" stroke="#666" fill="none" stroke-width="1.5"/></svg></span></div>
    <div class="abs hero-media" role="img" aria-label="Three server tower units standing side by side"></div>
  </section>

  <article class="abs service-card" style="left:118px">
    <div class="service-icon"><svg width="36" height="32" viewBox="0 0 36 32"><rect x="2" y="10" width="14" height="20" fill="#111"/><path d="M4 15h10M4 20h10M4 25h10" stroke="#fff"/><circle cx="23" cy="13" r="11" fill="#111"/><path d="M16 10h6l2 4-3 5M28 5l-2 6 5 3" stroke="#fff" fill="none"/></svg></div>
    <h3 class="service-title">Hosting</h3>
    <p class="service-text">Praesent vitae purus eu libero laoreet ornare. Ut justo quamet cursus neque. Fusce dui nibh auctor vel fermentum non</p>
    <div class="btn-small">Read More</div>
  </article>
  <article class="abs service-card" style="left:322px">
    <div class="service-icon"><svg width="40" height="34" viewBox="0 0 40 34"><rect x="2" y="4" width="36" height="22" fill="none" stroke="#111" stroke-width="3"/><path d="M14 26l-2 6h16l-2-6" fill="#111"/><path d="M12 20l18-18 3 3-18 18-4 1z" fill="#111"/></svg></div>
    <h3 class="service-title">Web &amp; Logo design</h3>
    <p class="service-text">Praesent vitae purus eu libero laoreet ornare. Ut justo quamet cursus neque. Fusce dui nibh auctor vel fermentum non</p>
    <div class="btn-small">Read More</div>
  </article>
  <article class="abs service-card" style="left:527px">
    <div class="service-icon"><svg width="40" height="40" viewBox="0 0 40 40"><path d="M20 8v24M8 20h24" stroke="#111" stroke-width="3"/><rect x="13" y="1" width="14" height="10" fill="#111"/><rect x="13" y="29" width="14" height="10" fill="#111"/><rect x="1" y="15" width="14" height="10" fill="#111"/><rect x="25" y="15" width="14" height="10" fill="#111"/></svg></div>
    <h3 class="service-title">ICT Systems Management</h3>
    <p class="service-text">Praesent vitae purus eu libero laoreet ornare. Ut justo quamet cursus neque. Fusce dui nibh auctor vel fermentum non</p>
    <div class="btn-small">Read More</div>
  </article>

  <h2 class="abs section-title" style="left:118px">Welcome To <b>VQ Services</b></h2>
  <div class="abs rule" style="left:118px;width:270px"></div>
  <div class="abs welcome-media" role="img" aria-label="Server racks and a monitor showing a world map under a cloudy sky"></div>
  <p class="abs welcome-text">Vestibulum quis felis ut enim aliquam iaculis. Nullam pharetra tortor at quam viverra volutpat. Phasellus vel faucibus dolor. Curabitur ac nisi non metus dignissim dapibus eu vel nibh. Phasellus semper dictum dapibus. Vestibulum quis felis ut enim aliquam iaculis. Nullam pharetra tortor at quam viverra volutpat. Phasellus vel faucibus dolor. Curabitur ac nisi non metus dignissim dapibus eu vel nibh. Phasellus semper dictum dapibus. Vestibulum quis felis ut enim aliquam iaculis. Nullam pharetra tortor at quam viverra volutpat.</p>
  <div class="abs btn-dark">Learn More</div>

  <h2 class="abs section-title" style="left:426px">News &amp; <b>Events</b></h2>
  <div class="abs rule" style="left:426px;width:284px"></div>
  <article class="abs news-item" style="top:760px">
    <div class="news-photo" role="img" aria-label="Portrait photo of a smiling businesswoman" style="background:linear-gradient(135deg,#e9e4de,#c9b29a 60%,#8d6e55)"></div>
    <h4 class="news-title">Class aptent taciti sociosqu</h4>
    <div class="news-date">March-22-2011</div>
    <p class="news-text">Lorem ipsum dolor sit amet, consectetuer adipiscing elit, sed diam nonummy nibh euismod tincidunt ut laoreet dolore magna aliquam erat volutpat.</p>
    <span class="news-more">Read More</span>
  </article>
  <article class="abs news-item" style="top:905px">
    <div class="news-photo" role="img" aria-label="Photo of a person working with charts at an office desk" style="background:linear-gradient(135deg,#d7c2a2,#e8eef3 50%,#7aa6cf)"></div>
    <h4 class="news-title">Class aptent taciti sociosqu</h4>
    <div class="news-date">March-22-2011</div>
    <p class="news-text">Lorem ipsum dolor sit amet, consectetuer adipiscing elit, sed diam nonummy nibh euismod tincidunt ut laoreet dolore magna aliquam erat volutpat.</p>
    <span class="news-more">Read More</span>
  </article>

  <div class="abs partners">
    <span class="partner">Tessaform</span>
    <span class="partner"><i></i>Orbisa</span>
    <span class="partner">Markpin</span>
    <span class="partner">Ambertrail</span>
    <span class="partner"><i></i>Outfold</span>
  </div>

  <footer class="abs site-footer">
    <div class="abs footer-brand">VQ Services</div>
    <div class="abs footer-nav">HOME &nbsp;| &nbsp;COMPANY &nbsp;| &nbsp;SERVICES | CLIENTS | &nbsp;CAREER | &nbsp;CONTACT US</div>
    <div class="abs footer-copy">©2014 2014 VQ Services, All Rights Reserved.</div>
    <span class="abs social" role="img" aria-label="Social link one" style="left:633px;background:#3aa3d8"></span>
    <span class="abs social" role="img" aria-label="Social link two" style="left:660px;background:#3e63a8"></span>
    <span class="abs social" role="img" aria-label="Social link three" style="left:687px;background:#555"></span>
  </footer>

</div>
</body>
</html>
```